Flyer "Pinch Analysis"-Energy Optimization procedure for Industry

We need a flyer (1xA4 recto/verso )design for a new part of our business.

In Summary: we want to communicate that we are providing "Pinch Analysis" for the industry. It's an energy optimization procedure. We are a cutting edge engineering consulting group.

All details about project in the attached files

Target Market(s)

Engineering

Industry/Entity Type

Business

Font styles to use
Serif

Requirements
Must have
• Finale document in .ai format ready for printing
• More informations in attached files
Nice to have
• See attached files

```html
<!DOCTYPE html>
<html lang="fr">
<head>
<meta charset="utf-8">
<title>Analyse Pinch – Flyer recto/verso</title>
<link href="https://fonts.googleapis.com/css2?family=Arimo:wght@400;700&family=Open+Sans:wght@400;600;700&family=Roboto+Condensed:ital,wght@0,400;0,700;1,400&display=swap" rel="stylesheet">
<style>
  :root{
    --backdrop:#e4e6e9;
    --paper:#f7f9fb;
    --navy:#1d3557;
    --navy-deep:#16294a;
    --sky:#2ea3e6;
    --sky-soft:#bfe2f7;
    --sky-pale:#e6f4fc;
    --text:#3d4654;
    --photo-steel-a:#6f7f90;
    --photo-steel-b:#2f3d4c;
    --photo-blue-a:#3a78b8;
    --photo-blue-b:#1c3a5c;
  }
  *{box-sizing:border-box;margin:0;padding:0}
  html,body{width:1200px;height:838px;overflow:hidden;background:var(--backdrop)}
  .canvas{position:relative;width:1200px;height:838px;overflow:hidden}
  .page{position:absolute;top:108px;width:496px;height:647px;background:var(--paper);overflow:hidden;box-shadow:0 4px 14px rgba(0,0,0,.18)}
  .page--verso{left:91px}
  .page--recto{left:612px}

  .page__foot{position:absolute;left:0;right:0;top:530px;bottom:0;
    background:linear-gradient(180deg,#fafcfe 0%,var(--sky-pale) 45%,var(--sky-soft) 100%)}

  .band{position:absolute;left:0;right:0;height:7px;background:var(--sky)}
  .photo{position:absolute;left:0;right:0;top:142px;height:273px}
  .photo--pipes{background:linear-gradient(160deg,var(--photo-steel-a) 0%,#95a4b3 35%,var(--photo-steel-b) 100%)}
  .photo--tanks{background:linear-gradient(150deg,#8996a4 0%,var(--photo-blue-a) 45%,var(--photo-blue-b) 100%)}

  /* verso */
  .intro{position:absolute;left:28px;top:20px;width:450px;font-family:"Arimo",sans-serif;font-weight:700;
    font-size:12.6px;line-height:1.33;color:var(--navy)}
  .questions{position:absolute;left:0;top:70px;list-style:none}
  .questions li{position:relative;height:18px;margin-bottom:0;padding-left:34px;
    font-family:"Open Sans",sans-serif;font-weight:600;font-size:9.4px;line-height:18px;color:var(--navy)}
  .questions .tab{position:absolute;left:0;top:3px;width:30px;height:12px}
  .cols{position:absolute;top:436px;left:26px;right:24px;display:flex;gap:0}
  .col{font-family:"Open Sans",sans-serif;font-size:6.7px;line-height:1.45;color:var(--text)}
  .col p{margin-bottom:9px}
  .col--left{width:236px;padding-right:18px}
  .col--right{width:210px;padding-left:18px;border-left:1px solid #9aa7b4;min-height:190px}
  .col strong{color:var(--navy-deep)}
  .col .gap{margin-top:26px}
  .contact{margin-top:30px}
  .contact__who{font-family:"Roboto Condensed",sans-serif;font-style:italic;font-size:9.5px;color:var(--navy)}
  .contact__who b{font-weight:700}
  .call{font-family:"Roboto Condensed",sans-serif;font-weight:700;color:var(--navy);letter-spacing:.2px}
  .contact .call{font-size:15.5px;margin-top:6px}
  .call small{font-size:.82em}
  .contact__addr{font-family:"Roboto Condensed",sans-serif;font-style:italic;font-size:7.5px;color:var(--text);margin-top:6px}

  /* recto */
  .brand{position:absolute;left:72px;top:28px;display:flex;align-items:center;gap:10px}
  .brand__mark{width:14px;height:14px;background:var(--sky)}
  .brand__name{font-family:"Arimo",sans-serif;font-weight:700;font-size:19px;letter-spacing:.5px;color:var(--navy);line-height:1.05}
  .web{position:absolute;left:45px;top:112px;width:288px;height:27px;
    font-family:"Roboto Condensed",sans-serif;font-weight:700;font-size:13px;color:#fff;
    display:flex;align-items:center;padding-left:24px}
  .web svg,.tag svg{position:absolute;inset:0;z-index:0}
  .web span,.tag span{position:relative;z-index:1}
  .tag{position:absolute;left:36px;top:420px;width:146px;height:25px;display:flex;align-items:center;justify-content:center;
    font-family:"Roboto Condensed",sans-serif;font-weight:700;font-size:15.5px;color:#fff;letter-spacing:.3px}
  .headline{position:absolute;left:20px;top:466px;width:266px;text-align:center;
    font-family:"Arimo",sans-serif;font-weight:700;font-size:17.2px;line-height:30px;color:var(--navy)}
  .page--recto .call{position:absolute;right:32px;top:609px;font-size:17px}
  .chart{position:absolute;pointer-events:none}
</style>
</head>
<body>
<main class="canvas">

  <!-- Verso -->
  <section class="page page--verso">
    <div class="page__foot"></div>
    <h2 class="intro">L'analyse Pinch est une méthode d'analyse systématique développée et appliquée depuis les années 1980; elle permet de répondre aux questions suivantes:</h2>
    <ul class="questions">
      <li><svg class="tab" viewBox="0 0 30 12"><polygon points="0,0 22,0 30,6 22,12 0,12" fill="#1d3557"/><circle cx="24" cy="6" r="4.4" fill="#2ea3e6"/><path d="M21.8 6l1.6 1.6 3-3.2" stroke="#fff" stroke-width="1.2" fill="none"/></svg>Quels sont les besoins de chaleur et de froid minimaux de mon procédé</li>
      <li><svg class="tab" viewBox="0 0 30 12"><polygon points="0,0 22,0 30,6 22,12 0,12" fill="#1d3557"/><circle cx="24" cy="6" r="4.4" fill="#2ea3e6"/><path d="M21.8 6l1.6 1.6 3-3.2" stroke="#fff" stroke-width="1.2" fill="none"/></svg>Quel est mon potentiel de réduction de consommation énergétique</li>
      <li><svg class="tab" viewBox="0 0 30 12"><polygon points="0,0 22,0 30,6 22,12 0,12" fill="#1d3557"/><circle cx="24" cy="6" r="4.4" fill="#2ea3e6"/><path d="M21.8 6l1.6 1.6 3-3.2" stroke="#fff" stroke-width="1.2" fill="none"/></svg>Quel est la solution technique présentant les coûts minimaux entre investissements et économies</li>
    </ul>
    <div class="band" style="top:134px"></div>
    <div class="photo photo--pipes" role="img" aria-label="Photo d'une installation industrielle: réseau dense de tuyauteries en acier et passerelles"></div>
    <div class="band" style="top:415px"></div>

    <div class="cols">
      <div class="col col--left">
        <p>La performance opérationnelle et l'efficacité énergétique sont les clés de la réussite de l'industrie de demain.</p>
        <p>Fort d'une longue expérience dans l'analyse, la conception et la mise en service d'installations industrielles (chimie, alimentaire, pharmacie,...), la société Northvale utilise l'analyse Pinch dans sa démarche de conception et d'amélioration.</p>
        <p class="gap">L'amélioration de l'efficacité énergétique est liée directement à l'exploitation des potentiels de récupération du procédé. Des potentiels de diminution de la consommation de 10 à 30% sont usuels. Nous pouvons également améliorer les performances opérationnelles en analysant vos méthodes de fabrication.</p>
        <p>L'analyse Pinch est aussi bien adaptée pour les PME que pour les grandes entreprises dont les procédés sont exploités de manière continue ou discontinue (batch).</p>
      </div>
      <div class="col col--right">
        <p>Etant donné les objectifs énergétiques de la confédération, <strong>l'agence nationale de l'énergie (ANE) soutient les analyses Pinch à hauteur de 35% pour les procédés continus et de 60% pour les procédés discontinus (batch).</strong></p>
        <p>Pour tous compléments d'informations et pour savoir si une analyse Pinch est justifiée dans votre cas, nous vous conseillons avec plaisir.</p>
        <div class="contact">
          <p class="contact__who"><b>Contact:</b> Lucien Marchand, Élise Fournier</p>
          <p class="call"><small>CALL NOW</small> 021-555-0147</p>
          <p class="contact__addr">Rue des Ateliers 14, CH-1950 Sion</p>
        </div>
      </div>
    </div>
  </section>

  <!-- Recto -->
  <section class="page page--recto">
    <div class="page__foot"></div>
    <div class="brand">
      <span class="brand__mark"></span>
      <span class="brand__name">NORTHVALE<br>PROCESS ENGINEERING</span>
    </div>
    <svg class="chart" style="left:330px;top:35px" width="166" height="100" viewBox="0 0 166 100">
      <polyline points="6,96 80,80 160,36 162,2" fill="none" stroke="#2ea3e6" stroke-width="1.6"/>
      <circle cx="80" cy="80" r="3.6" fill="#8a949e"/><circle cx="160" cy="36" r="3.6" fill="#8a949e"/>
    </svg>
    <div class="web">
      <svg viewBox="0 0 288 27" preserveAspectRatio="none"><polygon points="10,0 288,0 278,27 0,27" fill="#1d3557"/></svg>
      <span>www.northvaleprocess.com</span>
    </div>
    <div class="band" style="top:137px"></div>
    <div class="photo photo--tanks" role="img" aria-label="Photo d'une salle technique avec cuves bleues de traitement et tuyauteries"></div>
    <div class="band" style="top:415px"></div>
    <div class="tag">
      <svg viewBox="0 0 146 25" preserveAspectRatio="none"><polygon points="8,0 146,0 138,25 0,25" fill="#1d3557"/></svg>
      <span>Analyse Pinch</span>
    </div>
    <h1 class="headline">en route vers la performance opérationnelle et l'efficacité énergétique</h1>
    <svg class="chart" style="left:170px;top:420px" width="326" height="230" viewBox="0 0 326 230">
      <polyline points="8,225 86,170 162,146 192,46 320,2" fill="none" stroke="#2ea3e6" stroke-width="1.6"/>
      <polyline points="24,212 86,196" fill="none" stroke="#2ea3e6" stroke-width="1.2"/>
      <line x1="86" y1="170" x2="86" y2="150" stroke="#2ea3e6" stroke-width="1.2"/>
      <line x1="162" y1="146" x2="162" y2="128" stroke="#2ea3e6" stroke-width="1.2"/>
      <circle cx="18" cy="200" r="3.6" fill="#8a949e"/>
      <circle cx="86" cy="170" r="3.6" fill="#8a949e"/>
      <circle cx="162" cy="146" r="3.6" fill="#8a949e"/>
      <circle cx="192" cy="46" r="3.6" fill="#8a949e"/>
    </svg>
    <p class="call"><small>CALL NOW</small> 021-555-0147</p>
  </section>

</main>
</body>
</html>
```